Delcourt Realty Business Cards

Design business card

Target Market(s)

High-End Buyer of Real Estate over $1 million dollars

Industry/Entity Type

Realtor

Contact Information for Business Card

Lena Delcourt R(S) LIC.# 41972
Cell 555 246-1938
Email Lena@Delcourt.example
Website IsleFreshHomes.example

Also Need Cards for:

Hank Delcourt R(B) LIC# 69418
C 555 613-7052
E Hank@Delcourt.example
W IsleFreshHomes.example

Colors

Designer to choose colors to be used in the design.

Requirements
Must have
• Address on back:
• 287 Pohaku Cir. , Wailea HI 96753
• Logo on back
Nice to have
• I would like the phone numbers and email address to be big so people can read it easily
Should not have
• Very small print Except For: address (287 Pohaku Cir. Wailea HI 96753)

```html
<!DOCTYPE html>
<html lang="en">
<head>
<meta charset="utf-8">
<title>Delcourt Realty Business Cards</title>
<link rel="stylesheet" href="https://fonts.googleapis.com/css2?family=Montserrat:wght@400;500;600&display=swap">
<style>
  :root {
    --backdrop: #2b2d30;
    --card-black: #0c0c0d;
    --band-grey: #d9d9d9;
    --ink-white: #f4f4f4;
    --ink-soft: #c8c8c8;
    --ink-muted: #8a8a8a;
    --ink-dark: #1e1e1e;
    --photo-warm: #b98a78;
    --photo-cool: #3a3a40;
  }
  * { margin: 0; padding: 0; box-sizing: border-box; }
  html, body {
    width: 1200px; height: 900px; overflow: hidden;
    background: var(--backdrop);
    font-family: "Montserrat", sans-serif;
  }
  .sheet {
    width: 1200px; height: 900px;
    display: flex; align-items: center; justify-content: center; gap: 50px;
  }
  .card {
    position: relative;
    width: 525px; height: 300px;
    background: var(--card-black);
    border-radius: 4px;
    overflow: hidden;
    box-shadow: 0 14px 30px rgba(0,0,0,.45);
  }
  .card__band {
    position: absolute; left: 0; right: 0; bottom: 0;
    height: 44px;
    background: var(--band-grey);
    display: flex; align-items: center;
    padding: 0 32px;
    color: var(--ink-dark);
    white-space: nowrap;
  }

  /* Back of card */
  .card--back .brand-mark {
    position: absolute; left: 0; right: 0; top: 0; bottom: 44px;
    display: flex; align-items: center; justify-content: center; gap: 14px;
  }
  .brand-mark__square {
    width: 34px; height: 34px; background: var(--ink-white); border-radius: 3px;
  }
  .brand-mark__name {
    color: var(--ink-white);
    font-weight: 600; font-size: 26px; letter-spacing: 4px; text-transform: uppercase;
  }
  .card--back .card__band {
    justify-content: center;
    font-size: 14px; letter-spacing: 1px; font-weight: 500;
  }

  /* Front of card */
  .agent-name {
    position: absolute; left: 32px; top: 34px;
    color: var(--ink-white);
    font-weight: 600; font-size: 40px; letter-spacing: 3px;
    white-space: nowrap;
  }
  .agent-license {
    position: absolute; left: 34px; top: 88px;
    color: var(--ink-muted);
    font-size: 10px; letter-spacing: 1px;
  }
  .contact {
    position: absolute; left: 32px; bottom: 62px;
  }
  .contact__brand {
    display: flex; align-items: center; gap: 10px;
    margin-bottom: 12px;
  }
  .contact__brand-square {
    width: 22px; height: 22px; background: var(--ink-white); border-radius: 2px;
  }
  .contact__brand-name {
    color: var(--ink-white);
    font-weight: 600; font-size: 15px; letter-spacing: 3px; text-transform: uppercase;
  }
  .contact__phone {
    color: var(--ink-white);
    font-size: 26px; letter-spacing: 2px; font-weight: 400;
    line-height: 1.25;
  }
  .contact__email {
    color: var(--ink-soft);
    font-size: 22px; font-weight: 400; letter-spacing: .5px;
    line-height: 1.3;
  }
  .agent-photo {
    position: absolute; right: 30px; bottom: 62px;
    width: 92px; height: 110px;
    border-radius: 3px;
    background: linear-gradient(160deg, var(--photo-cool) 0%, var(--photo-warm) 100%);
  }
  .card--front .card__band {
    justify-content: flex-start;
    font-size: 14px; letter-spacing: 1px;
  }
</style>
</head>
<body>
  <main class="sheet">
    <section class="card card--back" aria-label="Card back">
      <div class="brand-mark">
        <span class="brand-mark__square"></span>
        <span class="brand-mark__name">Delcourt Realty</span>
      </div>
      <div class="card__band">287 Pohaku Cir. , Palm Cove ST 00000</div>
    </section>

    <section class="card card--front" aria-label="Card front">
      <h1 class="agent-name">LENA DELCOURT</h1>
      <p class="agent-license">R(S) LIC.# 41972</p>
      <div class="contact">
        <div class="contact__brand">
          <span class="contact__brand-square"></span>
          <span class="contact__brand-name">Delcourt Realty</span>
        </div>
        <p class="contact__phone">555 246-1938</p>
        <p class="contact__email">Lena@Delcourt.example</p>
      </div>
      <div class="agent-photo" role="img" aria-label="Portrait photo of the two agents"></div>
      <div class="card__band">www.IsleFreshHomes.example</div>
    </section>
  </main>
</body>
</html>
```